Business card for wedding & event planning company

I'm looking for a well designed double sided business card to represent my wedding and event planning company.

It should include the fact we manage the following events:
Weddings, birthdays, conferences, product launches, fashion shows & conventions
in the following areas:
Wiltshire, Oxfordshire, Berkshire & London

My contact details to be included are:

Moira Pennock
07715 482036
moira@amberlarkcelebrations.co.uk
www.amberlarkcelebrations.co.uk

My logo can be found at the following Filevaultex location:
AI file: https://www.filevaultex.com/s/k4mprt8wn31b7hz/brandlogo_sourcefile.ai?dl=0
PNG file:
https://www.filevaultex.com/s/h9qsle2vbx07mnd/brandlogo_image.png?dl=0

Target Market(s)

women aged 30-55

Industry/Entity Type

Wedding

Contact Information for Business Card

in the following areas:

Moira Pennock
Event Planner
07715 482036

Font styles to use
Serif
Sans Serif
Script

Requirements
Must have
• Purple and white colour scheme
Should not have
• Black background
• Please don't submit any of the see-through business card designs.

```html
<!DOCTYPE html>
<html lang="en">
<head>
<meta charset="utf-8">
<title>Amber Lark Celebrations – Business Card</title>
<link rel="stylesheet" href="https://fonts.googleapis.com/css2?family=Open+Sans:wght@400;600;700&display=swap">
<style>
  :root {
    --plum: #862b8f;
    --plum-deep: #7a2683;
    --white: #ffffff;
    --ink: #1a1a1a;
    --backdrop: #eceef0;
    --frame-line: rgba(255,255,255,0.55);
  }
  * { box-sizing: border-box; margin: 0; padding: 0; }
  html, body {
    width: 1200px; height: 1000px; overflow: hidden;
    background: var(--backdrop);
    font-family: "Open Sans", Arial, sans-serif;
  }
  .sheet {
    width: 1200px; height: 1000px;
    display: flex; flex-direction: column; align-items: center; justify-content: center;
    gap: 40px;
  }
  .card {
    width: 660px; height: 427px; position: relative; overflow: hidden;
    box-shadow: 0 6px 18px rgba(0,0,0,0.12);
  }

  /* Front */
  .card--front { background: var(--white); }
  .front-band {
    position: absolute; left: 0; right: 0; top: 255px; height: 62px;
    background: var(--plum);
  }
  .brand {
    position: absolute; left: 56px; top: 150px; width: 250px;
    display: flex; flex-direction: column; align-items: center; gap: 8px;
  }
  .brand-mark {
    width: 46px; height: 46px; border-radius: 50%; background: var(--plum);
  }
  .brand-name {
    color: var(--plum); font-weight: 600; font-size: 21px; letter-spacing: 0.5px;
    text-align: center; line-height: 1.15;
    border-bottom: 1px solid #d9c3dc; padding-bottom: 6px;
  }
  .holder-name {
    position: absolute; left: 56px; top: 255px; width: 250px; height: 62px;
    display: flex; align-items: center; justify-content: center;
    color: var(--white); font-size: 27px; font-weight: 400; letter-spacing: 1.5px;
  }
  .contact {
    position: absolute; right: 28px; top: 150px;
    list-style: none; display: flex; flex-direction: column; gap: 7px;
  }
  .contact-item {
    display: flex; align-items: center; justify-content: flex-end; gap: 8px;
    font-size: 13px; font-weight: 700; color: var(--ink); letter-spacing: 0.6px;
  }
  .contact-icon { width: 15px; height: 15px; flex: none; }
  .contact-item:nth-child(2), .contact-item:nth-child(3) { margin-top: 0; }
  .contact-item.is-spaced { margin-top: 34px; }

  /* Back */
  .card--back {
    background: linear-gradient(160deg, var(--plum) 0%, var(--plum-deep) 100%);
    color: var(--white);
  }
  .back-frame {
    position: absolute; inset: 28px; border: 1px solid var(--frame-line);
  }
  .back-content {
    position: absolute; inset: 28px;
    display: flex; flex-direction: column; align-items: center; justify-content: center;
    text-align: center;
  }
  .services {
    font-size: 18px; font-weight: 400; line-height: 1.45; letter-spacing: 0.6px;
  }
  .areas {
    margin-top: 22px; font-size: 19px; font-weight: 700; letter-spacing: 0.6px;
  }
  .back-brand {
    margin-top: 26px; display: flex; flex-direction: column; align-items: center; gap: 8px;
  }
  .back-brand .brand-mark { background: var(--white); width: 40px; height: 40px; }
  .back-brand .brand-name {
    color: var(--white); font-size: 18px; border-bottom-color: var(--frame-line);
  }
</style>
</head>
<body>
<main class="sheet">

  <section class="card card--front" aria-label="Business card front">
    <div class="front-band"></div>
    <div class="brand">
      <span class="brand-mark" aria-hidden="true"></span>
      <span class="brand-name">Amber Lark Celebrations</span>
    </div>
    <div class="holder-name">Moira Pennock</div>
    <ul class="contact">
      <li class="contact-item">07715 482036
        <svg class="contact-icon" viewBox="0 0 16 16" aria-hidden="true">
          <circle cx="8" cy="8" r="7.5" fill="#862b8f"/>
          <path d="M5.2 4.2l1.4-.3.8 2-1 .7c.5 1.1 1.2 1.8 2.3 2.3l.7-1 2 .8-.3 1.4c-3.3.3-6.2-2.6-5.9-5.9z" fill="#fff"/>
        </svg>
      </li>
      <li class="contact-item is-spaced">www.amberlarkcelebrations.co.uk
        <svg class="contact-icon" viewBox="0 0 16 16" aria-hidden="true">
          <circle cx="8" cy="8" r="7.5" fill="#862b8f"/>
          <circle cx="8" cy="8" r="4.3" fill="none" stroke="#fff" stroke-width="1"/>
          <ellipse cx="8" cy="8" rx="1.8" ry="4.3" fill="none" stroke="#fff" stroke-width="0.9"/>
          <path d="M3.7 8h8.6" stroke="#fff" stroke-width="0.9"/>
        </svg>
      </li>
      <li class="contact-item">moira@amberlarkcelebrations.co.uk
        <svg class="contact-icon" viewBox="0 0 16 16" aria-hidden="true">
          <circle cx="8" cy="8" r="7.5" fill="#862b8f"/>
          <rect x="4.2" y="5.2" width="7.6" height="5.6" fill="none" stroke="#fff" stroke-width="1"/>
          <path d="M4.2 5.4L8 8.4l3.8-3" fill="none" stroke="#fff" stroke-width="1"/>
        </svg>
      </li>
    </ul>
  </section>

  <section class="card card--back" aria-label="Business card back">
    <div class="back-frame"></div>
    <div class="back-content">
      <p class="services">Weddings, birthdays, conferences, product launches,<br>fashion shows&amp; conventions in the following areas:</p>
      <p class="areas">Wiltshire, Oxfordshire, Berkshire &amp; London</p>
      <div class="back-brand">
        <span class="brand-mark" aria-hidden="true"></span>
        <span class="brand-name">Amber Lark Celebrations</span>
      </div>
    </div>
  </section>

</main>
</body>
</html>
```